Modern Billboard Ad for Criminal Defense Firm

10.5 x 36 We're looking for something to set us apart from the local competition. Looking for sleek and modern. We're a mid-sized firm in a small market city. We want to give the artist room to be creative on this one.
Thanks

Target Market(s)

Adult clients who have been charged with a crime/DWI

Industry/Entity Type

legal

Font styles to use
Serif
Sans Serif

Requirements
Must have
• Needs to have the firm name in large lettering. Law Offices of Marcus T Whitfield. “PLLC” does not have to be included. Phone number of (555) 384-1927 should be included but not the main focus.
Nice to have
• A call to action or something similar. “Don’t go it alone, call today.”, “ Arrested?”

```html
<!DOCTYPE html>
<html lang="en">
<head>
<meta charset="utf-8">
<title>Billboard – Law Offices of Marcus T Whitfield</title>
<link rel="stylesheet" href="https://fonts.googleapis.com/css2?family=Michroma&family=Montserrat:wght@700;800&display=swap">
<style>
  :root {
    --page: #e6e9ec;
    --board-dark: #0e0f10;
    --board-mid: #2b2d2f;
    --rule: #d9d9d9;
    --text-light: #ececec;
    --accent: #2aa6dd;
    --accent-bright: #46c4ef;
    --photo-light: #b4b4b4;
    --photo-dark: #555555;
  }
  * { margin: 0; padding: 0; box-sizing: border-box; }
  html, body { width: 1200px; height: 900px; overflow: hidden; background: var(--page); }

  .billboard {
    position: absolute;
    left: 30px; top: 292px;
    width: 1140px; height: 316px;
    overflow: hidden;
    background:
      radial-gradient(ellipse at 65% 35%, rgba(255,255,255,0.12), transparent 60%),
      linear-gradient(180deg, var(--board-mid), var(--board-dark));
  }

  .accent-band { position: absolute; inset: 0; }

  .band-word {
    position: absolute;
    left: 356px; top: 230px;
    font-family: "Montserrat", sans-serif;
    font-weight: 800;
    font-size: 62px;
    line-height: 1;
    color: transparent;
    -webkit-text-stroke: 1px rgba(70,196,239,0.35);
    transform: rotate(-74deg);
    transform-origin: left top;
    white-space: nowrap;
    letter-spacing: 2px;
  }

  .portrait {
    position: absolute;
    left: 74px; top: 7px;
    width: 334px; height: 309px;
    background: linear-gradient(160deg, var(--photo-light) 0%, #8a8a8a 50%, var(--photo-dark) 100%);
  }

  .frame { position: absolute; inset: 0; pointer-events: none; }

  .award-badge {
    position: absolute;
    left: 43px; top: 43px;
    width: 56px; height: 79px;
    background: linear-gradient(180deg, #3b8fc4 0 22%, #1c1c1c 22% 80%, #2f8fc7 80%);
    border: 1px solid #5aa9d6;
  }

  .copy {
    position: absolute;
    left: 760px;
    transform: translateX(-50%);
    white-space: nowrap;
    text-align: center;
    line-height: 1;
  }

  .firm-name {
    top: 21px;
    font-family: "Michroma", sans-serif;
    font-size: 20px;
    color: var(--text-light);
  }

  .headline {
    top: 68px;
    font-family: "Montserrat", sans-serif;
    font-weight: 800;
    font-size: 100px;
    background: linear-gradient(180deg, var(--accent-bright), var(--accent));
    -webkit-background-clip: text;
    background-clip: text;
    color: transparent;
  }

  .tagline {
    top: 166px;
    font-family: "Michroma", sans-serif;
    font-size: 28px;
    color: var(--text-light);
  }

  .phone {
    top: 221px;
    display: flex; align-items: center; gap: 16px;
    font-family: "Montserrat", sans-serif;
    font-weight: 700;
    font-size: 58px;
    letter-spacing: 2px;
    color: var(--accent);
  }
  .phone-icon { width: 72px; height: 52px; }
</style>
</head>
<body>
  <div class="billboard">
    <svg class="accent-band" viewBox="0 0 1140 316" aria-hidden="true">
      <defs>
        <linearGradient id="bandFade" x1="0" y1="0" x2="1" y2="1">
          <stop offset="0" stop-color="#2a7f93" stop-opacity="0.7"/>
          <stop offset="1" stop-color="#14333b" stop-opacity="0.5"/>
        </linearGradient>
      </defs>
      <polygon points="338,0 470,0 490,316 380,316" fill="url(#bandFade)"/>
    </svg>
    <div class="band-word" aria-hidden="true">ARREST</div>

    <div class="portrait" role="img" aria-label="Black and white portrait of the attorney in a vest and tie, jacket slung over his shoulder"></div>

    <svg class="frame" viewBox="0 0 1140 316" aria-hidden="true">
      <g stroke="var(--rule)" stroke-width="1.5" fill="none">
        <polyline points="204,31 32,31 32,297 47,297"/>
        <polyline points="1065,31 1109,31 1109,299 427,299"/>
      </g>
    </svg>

    <div class="award-badge" role="img" aria-label="Award badge"></div>

    <div class="copy firm-name">LAW OFFICES OF MARCUS T WHITFIELD</div>
    <div class="copy headline">ARRESTED?</div>
    <div class="copy tagline">DON’T GO IT ALONE, CALL TODAY</div>
    <div class="copy phone">
      <svg class="phone-icon" viewBox="0 0 72 52" aria-hidden="true">
        <path d="M4 16 C4 4 68 4 68 16 L68 22 L54 22 L54 14 C46 11 26 11 18 14 L18 22 L4 22 Z" fill="var(--accent)"/>
        <path d="M22 18 L50 18 L62 40 L62 50 L10 50 L10 40 Z" fill="var(--accent)"/>
        <g fill="#141516">
          <rect x="28" y="26" width="4" height="4"/><rect x="34" y="26" width="4" height="4"/><rect x="40" y="26" width="4" height="4"/>
          <rect x="28" y="32" width="4" height="4"/><rect x="34" y="32" width="4" height="4"/><rect x="40" y="32" width="4" height="4"/>
          <rect x="28" y="38" width="4" height="4"/><rect x="34" y="38" width="4" height="4"/><rect x="40" y="38" width="4" height="4"/>
        </g>
      </svg>
      <span>(555) 384-1927</span>
    </div>
  </div>
</body>
</html>
```